Website Upgrade

Create new look for existing website: www.lunarisgrove.ca . You will find details on what we are about on the website. Email us at lunaris.grove@mailbright.ca if you have any questions. We will be more than happy to answer.
Lunaris grove is a website for women focused on empowering women.
Website must:
1. Be able to stream videos
2. Use of blogs
3. Purple must be one of the colours used in the scheme.
4. Must use existing lunaris grove logo (purple head with 'Lunaris Grove' script in white.. see on homepage). However, we are open to new logo suggestions
5. Must be professional. We are trendy but not boring.

```html
<!DOCTYPE html>
<html lang="en">
<head>
<meta charset="utf-8">
<title>Lunaris Grove</title>
<link href="https://fonts.googleapis.com/css2?family=Nunito:wght@400;600;700&family=Open+Sans:wght@400;600&display=swap" rel="stylesheet">
<style>
:root{
  --purple:#8a2aa6;
  --purple-dark:#6a1787;
  --purple-light:#a23fbe;
  --plum:#8c1a6e;
  --ink:#111;
  --text:#666;
  --muted:#777;
  --line:#e2e2e2;
  --footer-bg:#f7f6f8;
  --white:#fff;
}
*{box-sizing:border-box;margin:0;padding:0}
html,body{width:1190px;height:1200px;overflow:hidden;background:var(--white)}
body{position:relative;font-family:"Open Sans",Arial,sans-serif;color:var(--text)}
.abs{position:absolute}
.heading{font-family:"Nunito",Arial,sans-serif}

/* header */
.brand{left:150px;top:42px;display:flex;align-items:center;gap:10px}
.brand-mark{width:30px;height:30px;border-radius:50%;background:var(--purple)}
.brand-name{font-family:"Nunito",Arial,sans-serif;font-weight:600;font-size:27px;color:var(--purple-dark);letter-spacing:.5px}
.social{left:964px;top:75px;display:flex;gap:8px}
.social span{width:21px;height:21px;border-radius:2px}
.social .s1{background:#3b5b99}.social .s2{background:#5bb7e6}.social .s3{background:#1c73a8}

/* nav */
.nav{left:0;top:111px;width:1190px;height:48px;background:linear-gradient(#9a3bb8,var(--purple) 55%,#7a1f98);display:flex;padding-left:165px}
.nav a{font-family:"Nunito",Arial,sans-serif;font-size:16px;color:var(--white);text-decoration:none;padding:0 24px;line-height:48px;border-right:1px solid rgba(255,255,255,.35)}
.nav a:last-child{border-right:0}

/* hero */
.hero{left:0;top:159px;width:1190px;height:429px;background:#fbfbfb;border-bottom:1px solid var(--line)}
.hero-photo{left:420px;top:159px;width:770px;height:428px;background:
  radial-gradient(ellipse 190px 230px at 62% 45%,#e6cfc6 0,#d9b8ab 45%,rgba(217,184,171,0) 100%),
  radial-gradient(ellipse 330px 300px at 58% 55%,#1e1a1e 0,#2c262b 55%,rgba(44,38,43,0) 100%),
  linear-gradient(90deg,#fbfbfb,#f4f2f4 40%,#eceaf0)}
.hero-kicker{left:151px;top:260px;font-size:24px;color:var(--plum);font-weight:600}
.hero-title{left:150px;top:292px;font-size:31px;line-height:41px;color:var(--ink);font-weight:600}
.hero-text{left:151px;top:376px;width:360px;font-size:12.5px;line-height:20px;color:var(--muted)}
.btn{left:150px;top:424px;width:130px;height:32px;border-radius:3px;background:linear-gradient(#9b40b8,var(--purple-dark));color:var(--white);font-family:"Nunito",Arial,sans-serif;font-size:12px;font-weight:700;text-align:center;line-height:32px}
.dots{left:152px;top:471px;display:flex;gap:3px}
.dots span{width:11px;height:11px;border-radius:50%;background:#777}

/* intro */
.intro-title{left:0;width:1190px;top:620px;text-align:center;font-size:34px;color:var(--purple-light);font-weight:400}
.intro-text{left:170px;width:850px;top:668px;text-align:center;font-size:12px;line-height:20px;color:var(--muted)}
.intro-fade{left:0;top:700px;width:1190px;height:52px;background:linear-gradient(rgba(240,238,242,0),#f4f2f5 70%,var(--white))}
.scroll-btn{left:583px;top:724px;width:46px;height:46px;border-radius:50%;background:var(--purple)}

/* videos */
.section-title{font-size:24px;top:794px;font-weight:400}
.videos-title{left:150px;color:var(--purple-light)}
.blog-title{left:641px;color:var(--ink)}
.video-card{top:838px;width:218px;height:141px;border:1px solid #ddd;padding:4px;background:var(--white);box-shadow:0 1px 3px rgba(0,0,0,.12)}
.video-card .thumb{width:100%;height:100%;position:relative}
.v1{left:150px}.v2{left:379px}
.v1 .thumb{background:linear-gradient(#b8c6dc,#a994b8 60%,#7d4e9a)}
.v2 .thumb{background:linear-gradient(100deg,#e7d6c4,#cfe3f0 60%,#a8cde8)}
.play{position:absolute;left:50%;top:50%;width:32px;height:32px;margin:-16px 0 0 -16px;border-radius:50%;background:var(--white)}
.play svg{display:block}
.video-name{top:990px;font-size:17px;color:#444}
.video-desc{top:1013px;width:215px;font-size:11px;line-height:18px;color:var(--muted)}

/* blog */
.blog-img{left:642px;width:104px;border:1px solid #ddd}
.b1{top:840px;height:70px;background:linear-gradient(120deg,#d6b88c,#b48c66 55%,#3a2a24)}
.b2{top:959px;height:69px;background:linear-gradient(120deg,#6c6c6c,#2a2a2a 60%,#4d4d4d)}
.blog-head{left:763px;font-size:16px;color:#444}
.blog-text{left:763px;width:280px;font-size:11.5px;line-height:18px;color:var(--muted)}
.blog-link{left:763px;font-size:12px;color:var(--purple-dark)}

/* footer */
.footer{left:0;top:1097px;width:1190px;height:103px;background:linear-gradient(#f3f2f4,var(--footer-bg) 20%,var(--footer-bg))}
.footer-nav{left:152px;top:1127px;font-family:"Nunito",Arial,sans-serif;font-size:14.5px;color:var(--purple-dark)}
.footer-nav b{font-weight:400;color:#555;margin:0 5px}
.copyright{left:152px;top:1157px;font-size:11.5px;color:var(--muted)}
</style>
</head>
<body>

<header>
  <div class="abs brand"><span class="brand-mark"></span><span class="brand-name">Lunaris Grove</span></div>
  <div class="abs social" aria-label="Social links"><span class="s1"></span><span class="s2"></span><span class="s3"></span></div>
</header>

<nav class="abs nav">
  <a>HOME</a><a>ABOUT US</a><a>LUNARIS GROVE</a><a>FAQ</a><a>OUR BLOGS</a><a>CONTACT US</a>
</nav>

<section>
  <div class="abs hero"></div>
  <div class="abs hero-photo" role="img" aria-label="Portrait of a woman with long dark wavy hair on a light background"></div>
  <div class="abs heading hero-kicker">EMBODY YOUR RADIANCE,</div>
  <div class="abs heading hero-title">MAGNETISM, AND<br>FEMININE POWER NOW</div>
  <p class="abs hero-text">Suspendisse vulputate aliquam dui Nulla elementum dui ut augue Aliquam vehicula mi at mauris Maecena</p>
  <div class="abs btn">READ MORE</div>
  <div class="abs dots"><span></span><span></span><span></span><span></span></div>
</section>

<section>
  <h1 class="abs heading intro-title">Mauris vel lacus vitae felis vestibulum</h1>
  <p class="abs intro-text">Vivamus porttitor g purus nisi eleifend libero a tempus libero lectus feugiat felis Morbi diam mauris viverra in gravida eu mattis in ante Morbi eget arcu Morbi porta libero id ullamcorper nonummy nibh ligula pulvinar metus eget consectetuer augue nisi quis lacus Ut ac mi quis lacus mollis aliquam</p>
  <div class="abs intro-fade"></div>
  <div class="abs scroll-btn"><svg width="46" height="46" viewBox="0 0 46 46"><path d="M15 20l8 8 8-8" fill="none" stroke="#fff" stroke-width="2"/></svg></div>
</section>

<section>
  <h2 class="abs heading section-title videos-title">Latest Videos</h2>
  <div class="abs video-card v1"><div class="thumb" role="img" aria-label="Video still of a smiling woman doing yoga outdoors"><span class="play"><svg width="32" height="32" viewBox="0 0 32 32"><path d="M13 10l9 6-9 6z" fill="#111"/></svg></span></div></div>
  <div class="abs video-card v2"><div class="thumb" role="img" aria-label="Video still of a smiling blonde woman by the sea"><span class="play"><svg width="32" height="32" viewBox="0 0 32 32"><path d="M13 10l9 6-9 6z" fill="#111"/></svg></span></div></div>
  <div class="abs heading video-name" style="left:151px">Video Tittle</div>
  <div class="abs heading video-name" style="left:380px">Video Tittle</div>
  <p class="abs video-desc" style="left:151px">Morbi eget arcu Morbi porta libero id ullamcorper nonummy nibh lig</p>
  <p class="abs video-desc" style="left:380px">Morbi eget arcu Morbi porta libero id ullamcorper nonummy</p>
</section>

<section>
  <h2 class="abs heading section-title blog-title">Recent Blog</h2>
  <div class="abs blog-img b1" role="img" aria-label="Blog photo of a smiling dark-haired woman"></div>
  <div class="abs heading blog-head" style="top:838px">Donec scelerisque leo ac risus</div>
  <p class="abs blog-text" style="top:861px">Morbi porta libero id ullamcorper nonummy nibh ligula pulvinar metus eget consectetuer augue nisi quis lacus Ut ac mi</p>
  <div class="abs blog-link" style="top:919px">Read full story</div>
  <div class="abs blog-img b2" role="img" aria-label="Blog photo of a woman in sportswear"></div>
  <div class="abs heading blog-head" style="top:956px">Donec scelerisque leo ac risus</div>
  <p class="abs blog-text" style="top:979px">Morbi porta libero id ullamcorper nonummy nibh ligula pulvinar metus eget consectetuer augue</p>
  <div class="abs blog-link" style="top:1019px">Read full story</div>
</section>

<footer>
  <div class="abs footer"></div>
  <div class="abs footer-nav">HOME<b>|</b>ABOUT US<b>|</b>LUNARIS GROVE<b>|</b>FAQ<b>|</b>OUR BLOGS<b>|</b>CONTACT US</div>
  <div class="abs copyright">© 2014 Company Name&nbsp; All right reserved&nbsp; Term of Use</div>
</footer>

</body>
</html>
```